3 glossy INFOGRAPHIC SPLASH PAGES for website of video production / photography studio website

Hello. We need 3 designed infographic images to act as 'splash pages' on our work-in-progress website to offer detailed information to visitors.
1. MUDMAP
2. RATECARD
3. STUDIO FLOORPLAN

To view the website WIP - Go here: http://www.pindlevault.com.au/brellak/

Regarding FILE SIZES:

The MUDMAP should sit in landscape with dimensions 2048px wide x 1536px high.

The RATECARD and STUDIO FLOORPLAN should be laid out in PORTRAIT with dimensions 1526px wide x 2048px high.

Regarding DESIGNS:

First is a 'MUD MAP' that details travel and parking directions for visitors to our studio,

Second is a floorplan of our studio space, and

Third is a Studio Hire Rate Card.

We want these images to utilise our new theme / branding / logos (attached) and ultimately these designs need to be easily read and understood.

Attached Files (may not be in order in brief, but here is my list):
FILE 1 - (2- Brellak Studios Floorplan Rough Thursday, 10 December 2015 03:49:32) is a rough sketch of the floorplan with pertinent details.

FILE 2 - (1-brellak_mudmap_sketch Thursday, 10 December 2015 03:49:33A) rough sketch of the MUDMAP we wish to create

FILE 3 - (Federation_Starfleet_Hull_23rd Thursday, 10 December 2015 03:49:33) is the font we have used on our website (and are happy to utilise in these designs too)

FILE 4 - ( 3-BrellakRateCard Thursday, 10 December 2015 03:49:33) contains the details required for the ratecard.

FILE 5 - ( StockBucket - B52-Shadow Thursday, 10 December 2015 03:49:33) This the font used in our logo - please use it too if you see fit.

FILE 6 - (brellak_gold_logo_stacked_1080 Thursday, 10 December 2015 03:49:33) - our logo stack over two lines - please use this in the three documents (or the one line) as you see fit.

FILE 7 - (Brellak_logo_for_web_row Thursday, 10 December 2015 03:49:33) Is the logo over one line (non-stacked). Again, please utilise this or the stacked logo in each document to act as branding.

FILE 8 - ( Brellak_logo_W Thursday, 10 December 2015 03:49:33) - This is purely the 'W' - please use this to identify brellak studios in the mudmap, and could also be placed in the centre of the studios floorplan.

FILE 9 - ( Brellak Website_WIP Thursday, 10 December 2015 03:49:34) This is a layout of our website as a WIP - Will give you an idea of the look and feel of the website thus far.

FILE 10 (YELLOW_GOLD_debc36 Thursday, 10 December 2015 03:49:34) - This is the gold colour we wish to use in type (for headings) - The RBG Value is: #debc36. This is NOT A prerequisite but if you choose to use gold in type or borders etc, then this the gold we wish to use.

FILE 11 - (brellak_website_mood_theme Thursday, 10 December 2015 03:49:34_) - These are the colours and moods employed on our website. Please utilise this theme as a style guide for your designs.

FILE 12 - (12: brellak_googlemaps_for_reference Thursday, 10 December 2015 04:00:03) This is a snapshot of the the google-map of the area and a guide to the MUDMAP we wish to create, although we only need the details provided in the sketch (SEE FILE 2 for MUDMAP SKETCH).

FILE 13 - (studio_floorplan_example Thursday, 10 December 2015 05:06:02) &

FILE 14 - (studio_floorplan_ex2 Thursday, 10 December 2015 05:06:03) are examples of studio floorplans and are a guide to the floorplan we also wish to create - We wish to also add our branding to this (See files 6 + 7) and a big golden W (see FILE 8) in the middle.

Target Market(s)

potential studio hire customers (mainly producers)

Industry/Entity Type

Film Production

Font styles to use
Sans Serif
Other font styles liked:
• I have supplied branding fonts to be used as you see fit.

Colors
fbed22
00a990
0292cd
fece3e
f78f20
f37122

Requirements
Must have
• Supplied logos and branding theme / colours (see attached).
• Predominantly gold colour (specific gold supplied) as well as utilising colour theme (see attached)
Nice to have
• Would be nice if all three images have a continuity in their layout / design

```html
<!DOCTYPE html>
<html lang="en">
<head>
<meta charset="utf-8">
<title>Brellak Studios – Studio Floorplan</title>
<link rel="stylesheet" href="https://fonts.googleapis.com/css2?family=Open+Sans:wght@400;600;700;800&display=swap">
<style>
  :root {
    --navy: #232d40;
    --gold: #debc36;
    --room: #dfbd33;
    --room-edge: #a88a2c;
    --cream: #f3e49a;
    --ink: #1f2a3a;
    --white: #ffffff;
  }
  html, body {
    margin: 0;
    padding: 0;
    width: 894px;
    height: 1200px;
    overflow: hidden;
    background: var(--navy);
  }
  .floorplan {
    display: block;
    width: 894px;
    height: 1200px;
    font-family: "Open Sans", Arial, sans-serif;
  }
  .studio-title { fill: var(--gold); font-weight: 800; font-size: 54px; letter-spacing: 5px; }
  .dim-label { fill: var(--cream); font-size: 20px; }
  .dim-label--room { fill: var(--ink); font-weight: 700; font-size: 29px; }
  .dim-label--vertical { fill: var(--cream); font-size: 40px; }
  .count-label { fill: var(--cream); font-size: 17px; letter-spacing: 1px; }
  .room-label { fill: var(--ink); font-size: 18px; }
  .room-name { fill: var(--ink); font-weight: 800; font-size: 44px; letter-spacing: 3px; }
  .backdrop-label { fill: var(--ink); font-size: 20px; }
  .legend-title { fill: var(--cream); font-weight: 700; font-size: 18px; }
  .legend-item { fill: var(--cream); font-weight: 700; font-size: 17px; }
  .room-wall { fill: var(--room); stroke: var(--room-edge); stroke-width: 5; }
  .door-leaf { fill: var(--cream); stroke: var(--ink); stroke-width: 2; }
  .arrow-cream { stroke: var(--cream); stroke-width: 4; fill: none; }
  .arrow-ink { stroke: var(--ink); stroke-width: 4; fill: none; }
  .backdrop { fill: var(--white); }
  .legend-box { fill: none; stroke: var(--gold); stroke-width: 3; }
  .icon-ink { color: var(--ink); }
  .icon-cream { color: var(--cream); }
</style>
</head>
<body>
<svg class="floorplan" viewBox="0 0 894 1200" xmlns="http://www.w3.org/2000/svg" aria-label="Brellak Studios floorplan">
  <defs>
    <marker id="head-cream" viewBox="0 0 10 10" refX="8" refY="5" markerWidth="4" markerHeight="4" orient="auto-start-reverse">
      <path d="M0 0 L10 5 L0 10 Z" fill="#f3e49a"/>
    </marker>
    <marker id="head-ink" viewBox="0 0 10 10" refX="8" refY="5" markerWidth="4" markerHeight="4" orient="auto-start-reverse">
      <path d="M0 0 L10 5 L0 10 Z" fill="#1f2a3a"/>
    </marker>
    <symbol id="outlet-10" viewBox="0 0 40 36">
      <rect x="1.5" y="1.5" width="37" height="33" rx="16" fill="none" stroke="currentColor" stroke-width="2"/>
      <path d="M14 10 L12 15 M26 10 L28 15 M20 21 V27" stroke="currentColor" stroke-width="2" fill="none"/>
    </symbol>
    <symbol id="outlet-15" viewBox="0 0 44 40">
      <rect x="1.5" y="1.5" width="41" height="37" rx="18" fill="none" stroke="currentColor" stroke-width="2"/>
      <rect x="5" y="5" width="34" height="30" rx="15" fill="none" stroke="currentColor" stroke-width="2"/>
      <path d="M16 12 L14 17 M28 12 L30 17 M22 22 V29" stroke="currentColor" stroke-width="2" fill="none"/>
    </symbol>
    <symbol id="ethernet" viewBox="0 0 52 30">
      <path d="M10 4 L3 15 L10 26 M42 4 L49 15 L42 26" stroke="currentColor" stroke-width="4" fill="none"/>
      <circle cx="18" cy="15" r="2.6" fill="currentColor"/>
      <circle cx="26" cy="15" r="2.6" fill="currentColor"/>
      <circle cx="34" cy="15" r="2.6" fill="currentColor"/>
    </symbol>
  </defs>

  <!-- Heading -->
  <text class="studio-title" x="447" y="102" text-anchor="middle">BRELLAK STUDIOS</text>

  <!-- Door -->
  <text class="dim-label" x="311" y="195" text-anchor="middle">DOUBLE DOOR ACCESS - 3M</text>
  <line class="arrow-cream" x1="177" y1="218" x2="453" y2="218" marker-start="url(#head-cream)" marker-end="url(#head-cream)"/>

  <!-- Room -->
  <rect class="room-wall" x="76" y="242" width="476" height="892"/>
  <rect class="door-leaf" x="175" y="237" width="142" height="17"/>
  <rect class="door-leaf" x="317" y="237" width="140" height="17"/>

  <line class="arrow-ink" x1="97" y1="318" x2="531" y2="318" marker-start="url(#head-ink)" marker-end="url(#head-ink)"/>
  <text class="dim-label--room" x="384" y="352" text-anchor="middle">5M</text>

  <!-- Length -->
  <line class="arrow-cream" x1="588" y1="247" x2="588" y2="1133" marker-start="url(#head-cream)" marker-end="url(#head-cream)"/>
  <g class="dim-label--vertical" text-anchor="middle">
    <text x="640" y="380">9</text>
    <text x="640" y="438">.</text>
    <text x="640" y="483">5</text>
    <text x="640" y="547">M</text>
    <text x="640" y="599">E</text>
    <text x="640" y="651">T</text>
    <text x="640" y="703">R</text>
    <text x="640" y="755">E</text>
    <text x="640" y="807">S</text>
  </g>

  <!-- Upper points -->
  <text class="count-label" x="52" y="432" text-anchor="middle">1X</text>
  <use href="#outlet-15" class="icon-ink" x="100" y="406" width="44" height="40"/>
  <text class="count-label" x="52" y="490" text-anchor="middle">4X</text>
  <use href="#outlet-10" class="icon-ink" x="103" y="464" width="40" height="36"/>
  <use href="#ethernet" class="icon-ink" x="480" y="403" width="52" height="30"/>
  <text class="room-label" x="454" y="486" text-anchor="middle">4X</text>
  <use href="#outlet-10" class="icon-ink" x="487" y="460" width="40" height="36"/>

  <!-- Centre name -->
  <text class="room-name" x="323" y="696" text-anchor="middle">BRELLAK</text>

  <!-- Lower points -->
  <use href="#ethernet" class="icon-ink" x="92" y="833" width="52" height="30"/>
  <text class="room-label" x="453" y="853" text-anchor="end">4X FLOOR</text>
  <use href="#outlet-10" class="icon-ink" x="479" y="828" width="40" height="36"/>
  <use href="#outlet-10" class="icon-ink" x="100" y="892" width="40" height="36"/>
  <text class="room-label" x="170" y="911">8 -10 amp</text>
  <text class="room-label" x="170" y="935">Power Outlet</text>
  <text class="room-label" x="450" y="918" text-anchor="end">4X CEILING</text>
  <use href="#outlet-10" class="icon-ink" x="480" y="894" width="40" height="36"/>

  <!-- Backdrop -->
  <text class="backdrop-label" x="313" y="1064" text-anchor="middle">STUDIO BACKDROP (WHITE) - 4M</text>
  <line class="arrow-ink" x1="125" y1="1098" x2="497" y2="1098" marker-start="url(#head-ink)" marker-end="url(#head-ink)"/>
  <rect class="backdrop" x="125" y="1122" width="374" height="9"/>

  <!-- Legend -->
  <rect class="legend-box" x="617" y="915" width="258" height="199"/>
  <text class="legend-title" x="680" y="949">LEGENDS :</text>
  <use href="#outlet-10" class="icon-cream" x="634" y="970" width="29" height="26"/>
  <text class="legend-item" x="678" y="989">10 amp Power Outlet</text>
  <use href="#outlet-15" class="icon-cream" x="633" y="1021" width="32" height="29"/>
  <text class="legend-item" x="678" y="1042">15 amp Power Outlet</text>
  <use href="#ethernet" class="icon-cream" x="632" y="1074" width="34" height="20"/>
  <text class="legend-item" x="680" y="1091">Ethernet Port</text>
</svg>
</body>
</html>
```